Design the Keystone HR business card for my new business

I've just had a logo designed (attached) for my new business doing HR consulting. I'm a one person operation at this stage, my aim is to provide support and help to small to medium sized businesses with their people objectives or issues.

I'm not really into anything overly flashy, I'm not a PR or marketing agency. I'd like my card to look modern, professional and not gimmicky.

I'm thinking black front (to go with logo), double sided with details on the back, maybe in a different colour?

Logo attached in several different formats.

Front of the card to have logo and added text: People and Development Solutions

Back of the card to also feature logo in some way and say:
Megan Turlow
PO Box (TBA)
Marnoo Flats QLD 4381
0427 318 562
megan@keystonehr-example.com.au
www.keystonehr-example.com.au

Target Market(s)

Small to medium businesses / business owners.

Industry/Entity Type

Marketing

Requirements
Must have
• Double sided business card.
Should not have
• Anything overly gimmicky.

```html
<!DOCTYPE html>
<html lang="en">
<head>
<meta charset="utf-8">
<title>Keystone HR – Business Card</title>
<link href="https://fonts.googleapis.com/css2?family=Source+Sans+3:ital,wght@0,300;0,400;0,600;1,400;1,600&display=swap" rel="stylesheet">
<style>
  :root {
    --page: #ffffff;
    --card-front: #000000;
    --card-back: #8c8c8c;
    --text-light: #ffffff;
    --accent: #8e3a9d;
    --accent-bright: #a13bc0;
  }
  * { margin: 0; padding: 0; box-sizing: border-box; }
  html, body {
    width: 1008px;
    height: 1200px;
    overflow: hidden;
    background: var(--page);
    font-family: "Source Sans 3", "Myriad Pro", Arial, sans-serif;
  }
  .sheet { position: relative; width: 1008px; height: 1200px; }

  .card { position: absolute; left: 52px; width: 900px; }
  .card--front { top: 64px; height: 511px; background: var(--card-front); }
  .card--back { top: 635px; height: 514px; background: var(--card-back); }

  .brand-mark { position: absolute; display: block; }
  .brand-name {
    position: absolute;
    font-weight: 300;
    color: var(--text-light);
    white-space: nowrap;
    line-height: 1;
    letter-spacing: -0.5px;
  }

  .card--front .brand-mark { left: 364px; top: 58px; }
  .card--front .brand-name {
    left: 0; right: 0; top: 296px;
    text-align: center; font-size: 62px;
  }
  .tagline {
    position: absolute;
    left: 0; right: 0; top: 425px;
    text-align: center;
    font-style: italic;
    font-weight: 400;
    font-size: 25px;
    color: var(--accent);
  }

  .card--back .brand-mark { left: 148px; top: 98px; }
  .card--back .brand-name {
    left: 48px; width: 350px; top: 322px;
    text-align: center; font-size: 50px;
  }
  .divider {
    position: absolute;
    left: 400px; top: 156px;
    width: 2px; height: 208px;
    background: var(--text-light);
  }
  .contact {
    position: absolute;
    left: 450px; top: 112px;
    color: var(--text-light);
  }
  .contact__name { font-size: 30px; font-weight: 400; line-height: 1.2; }
  .contact__role {
    font-size: 29px; font-style: italic; font-weight: 400;
    color: var(--accent); line-height: 1.2;
  }
  .contact__details {
    list-style: none;
    margin-top: 52px;
    font-size: 24px;
    font-weight: 400;
    line-height: 34px;
  }
  .contact__web { color: var(--accent); }
</style>
</head>
<body>
<main class="sheet">
  <section class="card card--front" aria-label="Card front">
    <svg class="brand-mark" width="172" height="172" viewBox="0 0 172 172" aria-hidden="true">
      <circle cx="86" cy="86" r="80" fill="none" stroke="var(--accent-bright)" stroke-width="4"/>
    </svg>
    <p class="brand-name">Keystone HR</p>
    <p class="tagline">People and Development Solutions</p>
  </section>

  <section class="card card--back" aria-label="Card back">
    <svg class="brand-mark" width="150" height="150" viewBox="0 0 150 150" aria-hidden="true">
      <circle cx="75" cy="75" r="70" fill="none" stroke="var(--accent-bright)" stroke-width="4"/>
    </svg>
    <p class="brand-name">Keystone HR</p>
    <span class="divider" aria-hidden="true"></span>
    <div class="contact">
      <p class="contact__name">Megan Turlow</p>
      <p class="contact__role">Consultant</p>
      <ul class="contact__details">
        <li>PO Box (TBA)</li>
        <li>Marnoo Flats QLD 4381</li>
        <li>0427 318 562</li>
        <li>megan@keystonehr-example.com.au</li>
        <li class="contact__web">www.keystonehr-example.com.au</li>
      </ul>
    </div>
  </section>
</main>
</body>
</html>
```